I am a highly experienced private practice psychotherapist serving high end clientele in the Wall Street area of New York City. I need electronic letterhead (that can also be printed) to use for bills, receipts, and correspondences.

My clients are very high end and are used to elegance and wealth. The letterhead should contain the following information: Marian T. Holcombe, LCSW 72 Pellham Street, Suite 2561 New York, NY 10087 Phone : (917) 555-3194 email: therapy@marianholcombelcsw.example website: www.marianholcombelcsw.example

Thank you for your designs. Please be advised that the letterhead will be used for bills/invoices; professional letters to other mental health professionals and doctors, as well as to attorneys. It needs to be highly professional in the same way that a law firm has professional and elegant letterhead, raher than whimsical or with spa designers. My letters end up as official documents.

```html
<!DOCTYPE html>
<html lang="en">
<head>
<meta charset="utf-8">
<title>Marian T. Holcombe, LCSW — Letterhead</title>
<link href="https://fonts.googleapis.com/css2?family=Source+Sans+3:wght@400;600;700&display=swap" rel="stylesheet">
<style>
  :root {
    --ink: #111111;
    --paper: #ffffff;
    --plum: #97186f;
    --rule-dark: #8a8a8a;
    --rule-light: rgba(160,160,160,0);
  }
  * { margin: 0; padding: 0; box-sizing: border-box; }
  html, body { width: 927px; height: 1200px; overflow: hidden; background: var(--paper); }
  .letterhead {
    position: relative;
    width: 927px;
    height: 1200px;
    background: var(--paper);
    font-family: "Source Sans 3", "Myriad Pro", Arial, sans-serif;
    color: var(--ink);
  }
  .masthead { position: absolute; left: 31px; top: 20px; }
  .masthead__name {
    font-size: 30px;
    font-weight: 700;
    line-height: 1;
    letter-spacing: -0.2px;
  }
  .masthead__credential {
    margin-top: 3px;
    font-size: 19px;
    font-weight: 400;
    line-height: 1;
  }
  .masthead__rule { position: absolute; left: 0; top: 80px; width: 330px; height: 14px; }

  .contact-row {
    position: absolute;
    left: 24px;
    right: 22px;
    top: 1139px;
    display: flex;
    justify-content: space-between;
    align-items: center;
    font-size: 12px;
    font-weight: 700;
    letter-spacing: -0.3px;
    white-space: nowrap;
  }
  .contact-row__item { display: flex; align-items: center; gap: 3px; }
  .contact-row__icon { width: 15px; height: 15px; flex: none; }

  .footer-band { position: absolute; left: 0; width: 927px; }
  .footer-band--black { top: 1163px; height: 12px; background: var(--ink); }
  .footer-band--plum { top: 1175px; height: 25px; background: var(--plum); }
</style>
</head>
<body>
<div class="letterhead">
  <header class="masthead">
    <div class="masthead__name">Marian T. Holcombe</div>
    <div class="masthead__credential">LCSW</div>
  </header>
  <svg class="masthead__rule" viewBox="0 0 330 14" aria-hidden="true">
    <defs>
      <linearGradient id="ruleFade" x1="0" x2="1" y1="0" y2="0">
        <stop offset="0" stop-color="#b0b0b0" stop-opacity="0.3"/>
        <stop offset="0.35" stop-color="#7a7a7a"/>
        <stop offset="0.7" stop-color="#9a9a9a"/>
        <stop offset="1" stop-color="#cccccc" stop-opacity="0"/>
      </linearGradient>
    </defs>
    <path d="M0 4 Q165 1 330 4 Q165 12 0 6 Z" fill="url(#ruleFade)"/>
  </svg>

  <footer class="contact-row">
    <span class="contact-row__item">
      <svg class="contact-row__icon" viewBox="0 0 16 16" aria-hidden="true"><path d="M4 1h3l1 4-2 1.5c.8 1.8 2 3 3.5 3.5L11 8l4 1v3c0 1.5-1 2-2.5 2C6.5 14 2 9.5 2 3.5 2 2 2.5 1 4 1z" fill="var(--ink)"/></svg>
      (917) 555-3194
    </span>
    <span class="contact-row__item">
      <svg class="contact-row__icon" viewBox="0 0 16 16" aria-hidden="true"><path d="M8 1a5 5 0 0 0-5 5c0 4 5 9 5 9s5-5 5-9a5 5 0 0 0-5-5zm0 7.2A2.2 2.2 0 1 1 8 3.8a2.2 2.2 0 0 1 0 4.4z" fill="var(--ink)"/></svg>
      72 Pellham Street, Suite 2561 New York, NY 10087
    </span>
    <span class="contact-row__item">
      <svg class="contact-row__icon" viewBox="0 0 16 16" aria-hidden="true"><g fill="none" stroke="var(--ink)" stroke-width="1.4"><circle cx="8" cy="8" r="6.3"/><ellipse cx="8" cy="8" rx="2.8" ry="6.3"/><path d="M1.7 8h12.6M2.8 4.8h10.4M2.8 11.2h10.4"/></g></svg>
      www.marianholcombelcsw.example
    </span>
    <span class="contact-row__item">
      <svg class="contact-row__icon" viewBox="0 0 16 16" aria-hidden="true"><g fill="none" stroke="var(--ink)" stroke-width="1.4"><rect x="1.5" y="3.5" width="13" height="9" rx="1"/><path d="M1.8 4l6.2 5 6.2-5"/></g></svg>
      therapy@marianholcombelcsw.example
    </span>
  </footer>

  <div class="footer-band footer-band--black"></div>
  <div class="footer-band footer-band--plum"></div>
</div>
</body>
</html>
```